Velmar Diagnostics Website

Project Description – Velmar Website Design
We need a clean, modern, and professional website for Velmar Diagnostics, a Ashgrove Hale University of Brindlemoor spin-out focused on early cancer detection. Our first product, ThornaSCAN™, is a urine-based risk assessment test for pancreatic cancer, supported by strong clinical validation and partnerships with leading hospitals.

The site should:

Communicate trust, innovation, and clinical credibility.
Feature a clear value proposition on the home page with strong calls to action for investors, clinicians, and partners.
Showcase our technology, science, and clinical evidence in a way that is accessible but authoritative.
Highlight our university heritage, team, and collaborators.
Include sections for products/services, news/press, and contact forms.
Be fully responsive, WordPress compatible, SEO-friendly, and WCAG 2.1 AA accessible.

We want a minimalist, elegant design with subtle animations, strong visuals (e.g., science/biotech imagery), and a clear structure for future growth.
Deliverables should include editable design files (Figma/Sketch/Adobe XD) and a style guide.

```html
<!DOCTYPE html>
<html lang="en">
<head>
<meta charset="utf-8">
<title>Velmar Diagnostics</title>
<link href="https://fonts.googleapis.com/css2?family=Inter:wght@400;500;600;700&display=swap" rel="stylesheet">
<style>
:root{
  --blue:#3a86d9;
  --blue-deep:#2a6fc4;
  --blue-light:#7fc0ee;
  --yellow:#f6c02c;
  --ink:#111418;
  --muted:#555b63;
  --line:#d8dde3;
  --white:#ffffff;
}
*{box-sizing:border-box;margin:0;padding:0}
html,body{width:1200px;height:4659px;overflow:hidden}
body{position:relative;font-family:"Inter",sans-serif;color:var(--ink);background:var(--white)}
.btn{position:absolute;display:flex;align-items:center;justify-content:center;gap:8px;background:var(--yellow);color:var(--white);font-weight:600;font-size:14px;border-radius:20px;white-space:nowrap}
.btn .dot{width:13px;height:13px;border:1.5px solid var(--white);border-radius:50%;display:inline-block}
/* hero */
.hero{position:absolute;left:0;top:0;width:1200px;height:674px;background:linear-gradient(100deg,#3d86d6 0%,#4aa2e2 45%,#7cc6ee 70%,#3f7fcf 100%)}
.hero-virus{position:absolute;left:560px;top:100px;width:560px;height:500px;border-radius:50%;background:radial-gradient(circle,#1d4f9c 0%,#2c69b6 45%,rgba(60,130,210,0) 72%)}
.nav{position:absolute;left:150px;top:14px;width:900px;height:60px;background:var(--white);border-radius:30px;display:flex;align-items:center;padding:0 24px}
.brand{display:flex;align-items:center;gap:8px;color:var(--blue);font-weight:600;font-size:17px;letter-spacing:1px}
.brand .mark{width:20px;height:20px;border-radius:50%;background:var(--blue)}
.nav-links{position:absolute;left:295px;display:flex;gap:16px;font-size:14px;color:var(--ink)}
.nav-cta{left:719px;top:13px;width:158px;height:34px}
.hero h1{position:absolute;left:150px;top:192px;color:var(--white);font-size:46px;line-height:49px;font-weight:600;letter-spacing:-.3px}
.slider{position:absolute;left:150px;top:307px;display:flex;align-items:center;gap:12px;color:var(--white);font-size:13px}
.slider .c{width:24px;height:24px;border:1.5px solid rgba(255,255,255,.8);border-radius:50%}
.slider .bar{width:142px;height:3px;background:rgba(255,255,255,.5);position:relative}
.slider .bar::before{content:"";position:absolute;left:0;top:0;width:70px;height:3px;background:var(--yellow)}
.hero .sub{position:absolute;left:150px;top:372px;color:var(--white);font-size:17px}
.hero-cta{left:150px;top:446px;width:183px;height:36px}
.features{position:absolute;left:150px;top:584px;width:900px;height:157px;background:var(--white);border-radius:10px;box-shadow:0 8px 26px rgba(20,60,110,.14);display:flex;padding:28px 0}
.feature{padding:0 0 0 36px;border-left:1.5px solid var(--line);font-size:18px;line-height:21px;font-weight:500;white-space:nowrap}
.feature:nth-child(1){width:195px;border-left:none;padding-left:38px}
.feature:nth-child(2){width:192px}
.feature:nth-child(3){width:192px}
.feature:nth-child(4){width:321px}
.feature svg{display:block;margin-bottom:8px}
/* about */
.about-photo{position:absolute;left:150px;top:837px;width:517px;height:536px;border-radius:6px;background:linear-gradient(160deg,#c9d7e6 0%,#8fb1d8 50%,#5f8fca 100%)}
.about-card{position:absolute;left:589px;top:884px;width:461px;height:435px;background:var(--blue);border-radius:8px;color:var(--white);padding:30px 32px}
.about-card h2{font-size:34px;font-weight:500;margin-bottom:22px}
.about-card p{font-size:14px;line-height:26px;opacity:.95}
.about-card ul{list-style:none;margin-top:22px}
.about-card li{font-size:14px;line-height:41px;padding-left:22px;position:relative}
.about-card li::before{content:"";position:absolute;left:6px;top:18px;width:5px;height:5px;border-radius:50%;background:var(--white)}
.about-cta{left:32px;top:368px;width:184px;height:36px}
/* stats */
.stats-title{position:absolute;left:0;top:1466px;width:1200px;text-align:center;font-size:36px;line-height:41px;font-weight:500}
.stat{position:absolute;top:1599px;width:220px;height:172px}
.stat + .stat::before{content:"";position:absolute;left:-29px;top:8px;width:1.5px;height:160px;background:var(--line)}
.stat .num{font-size:42px;font-weight:500;letter-spacing:-1px}
.stat .lbl{display:flex;align-items:center;gap:10px;margin-top:14px;font-size:18px;line-height:20px;font-weight:500}
.stat .desc{margin-top:18px;font-size:10px;line-height:15px;color:var(--muted)}
/* product */
.product{position:absolute;left:0;top:1863px;width:1200px;height:542px;background:linear-gradient(90deg,#3a86d9 0%,#4a8fdc 30%,#9bbbe0 48%,#c8d3e0 70%,#aab8c8 100%);overflow:hidden}
.product .scene{position:absolute;left:430px;top:0;width:770px;height:542px;background:linear-gradient(90deg,rgba(58,134,217,0) 0%,rgba(190,200,215,.6) 40%,rgba(150,160,180,.5) 100%)}
.product h2{position:absolute;left:150px;top:90px;color:var(--white);font-size:36px;line-height:40px;font-weight:500}
.product p{position:absolute;left:150px;top:190px;width:290px;color:var(--white);font-size:14px;line-height:26px}
.product-cta{left:150px;top:436px;width:193px;height:36px}
/* services */
.services-title{position:absolute;left:150px;top:2496px;font-size:36px;font-weight:500}
.service{position:absolute;top:2600px;width:287px}
.service .img{height:327px}
.service h3{margin-top:14px;font-size:14px;font-weight:600;white-space:nowrap}
.service ul{list-style:none;margin-top:6px}
.service li{font-size:10.5px;line-height:23px;color:var(--muted);padding-left:16px;position:relative}
.service li::before{content:"";position:absolute;left:5px;top:10px;width:3px;height:3px;border-radius:50%;background:var(--muted)}
.read{margin-top:6px;font-size:10.5px;font-weight:600;display:flex;align-items:center;gap:6px}
.read span{width:10px;height:10px;border:1px solid var(--blue-light);border-radius:50%}
.services-cta{left:150px;top:3126px;width:193px;height:36px}
/* partner */
.partner-title{position:absolute;left:0;top:3254px;width:1200px;text-align:center;font-size:36px;font-weight:500}
.ring{position:absolute;top:3346px;width:210px;height:210px}
.ring .txt{position:absolute;inset:0;display:flex;flex-direction:column;align-items:center;justify-content:center}
.ring .pct{font-size:44px;font-weight:500;letter-spacing:-1px}
.ring .cap{font-size:18px;line-height:20px;text-align:center}
/* blog */
.blog-title{position:absolute;left:150px;top:3648px;font-size:36px;font-weight:500}
.blog-cta{left:858px;top:3652px;width:192px;height:36px}
.post{position:absolute;top:3740px;width:211px}
.post .img{height:211px}
.post .meta{display:flex;justify-content:space-between;margin-top:14px;font-size:8.5px;color:var(--muted)}
.post h4{margin-top:12px;font-size:13.5px;line-height:15px;font-weight:600}
/* footer */
.footer{position:absolute;left:0;top:4127px;width:1200px;height:532px;background:var(--blue);color:var(--white);overflow:hidden}
.footer .logo{position:absolute;left:310px;top:100px;width:580px;display:flex;align-items:center;justify-content:center;gap:26px;font-size:64px;font-weight:600;letter-spacing:6px}
.footer .logo .mark{width:88px;height:88px;border-radius:50%;background:var(--white)}
.footer .links{position:absolute;left:271px;top:292px;display:flex;gap:26px;font-size:14px}
.footer-cta{left:770px;top:284px;width:158px;height:34px}
.social{position:absolute;left:537px;top:360px;display:flex;gap:11px}
.social span{width:34px;height:34px;border-radius:50%;background:var(--white)}
.footer .rule{position:absolute;left:150px;top:463px;width:900px;height:1px;background:rgba(255,255,255,.6)}
.footer .legal{position:absolute;top:480px;font-size:9px}
.glow{position:absolute;border-radius:50%;background:rgba(255,255,255,.12)}
</style>
</head>
<body>

<section class="hero">
  <div class="hero-virus" role="img" aria-label="Blue 3D virus particles floating over a blue background"></div>
  <nav class="nav">
    <div class="brand"><span class="mark"></span>Velmar DX</div>
    <div class="nav-links"><span>Home</span><span>About Us</span><span>Products / Service</span><span>News</span><span>Contact</span></div>
    <span class="btn nav-cta">Get Started <i class="dot"></i></span>
  </nav>
  <h1>Lighting the Way to<br>Early Cancer Detection</h1>
  <div class="slider"><span class="c"></span><span>1 / 3</span><span class="bar"></span><span>❚❚</span><span class="c"></span></div>
  <p class="sub">highlight non-invasive, urine-based diagnostics.</p>
  <span class="btn hero-cta">Partner With Us <i class="dot"></i></span>
</section>

<div class="features">
  <div class="feature">
    <svg width="56" height="50" viewBox="0 0 56 50" fill="none" stroke="#3a86d9" stroke-width="2"><path d="M40 4l8 8L20 40l-8 2 2-8z"/><path d="M36 8l8 8"/><path d="M10 44l-6 4"/></svg>
    Non-invasive,<br>painless</div>
  <div class="feature">
    <svg width="56" height="50" viewBox="0 0 56 50" fill="none" stroke="#3a86d9" stroke-width="2"><circle cx="26" cy="22" r="12"/><path d="M35 31l12 12"/><rect x="4" y="4" width="12" height="14"/></svg>
    Precision<br>biomarkers</div>
  <div class="feature">
    <svg width="56" height="50" viewBox="0 0 56 50" fill="none" stroke="#3a86d9" stroke-width="2"><circle cx="24" cy="22" r="18"/><path d="M24 6v32M10 22h28"/><circle cx="16" cy="14" r="2"/><circle cx="32" cy="30" r="2"/></svg>
    AI-powered<br>insights</div>
  <div class="feature">
    <svg width="56" height="50" viewBox="0 0 56 50" fill="none" stroke="#3a86d9" stroke-width="2"><rect x="6" y="24" width="40" height="8"/><rect x="8" y="32" width="38" height="8"/><path d="M4 12l22-8 22 8-22 8z"/></svg>
    Clinically validated &amp;<br>university spin-out heritage</div>
</div>

<section>
  <div class="about-photo" role="img" aria-label="Clinician in blue scrubs holding two urine sample cups"></div>
  <div class="about-card">
    <h2>About Us</h2>
    <p>At Velmar Diagnostics, we believe early detection saves lives. Our mission is to combine breakthrough science with clinical expertise to make cancer testing simpler, safer, and more accessible worldwide.</p>
    <ul>
      <li>lectus risus varius lacus ridiculus at at aliquam. Enim</li>
      <li>Lorem ipsum dolor sit amet consectetur. Fusce et</li>
      <li>lectus risus varius lacus ridiculus at at aliquam. Enim</li>
    </ul>
    <span class="btn about-cta">Discover More <i class="dot"></i></span>
  </div>
</section>

<section>
  <h2 class="stats-title">Experience<br>The Best Results Every Time</h2>
  <div class="stat" style="left:150px"><div class="num">99%</div><div class="lbl"><svg width="48" height="46" viewBox="0 0 48 46" fill="none" stroke="#3a86d9" stroke-width="2"><path d="M36 4l8 8L18 38l-8 2 2-8z"/><path d="M4 42h20"/></svg>Scientific<br>Excellence</div><p class="desc">Backed by world-class cancer research<br>and clinical innovation.</p></div>
  <div class="stat" style="left:389px"><div class="num">320</div><div class="lbl"><svg width="48" height="46" viewBox="0 0 48 46" fill="none" stroke="#3a86d9" stroke-width="2"><circle cx="24" cy="12" r="6"/><path d="M12 42c0-10 5-16 12-16s12 6 12 16"/><circle cx="8" cy="22" r="4"/><circle cx="40" cy="22" r="4"/></svg>Professional<br>Team</div><p class="desc">Led by experienced scientists, clinicians,<br>and global advisors.</p></div>
  <div class="stat" style="left:629px"><div class="num">25+</div><div class="lbl"><svg width="48" height="46" viewBox="0 0 48 46" fill="none" stroke="#3a86d9" stroke-width="2"><rect x="6" y="8" width="30" height="34" rx="2"/><path d="M21 18v14M14 25h14"/><rect x="14" y="4" width="14" height="6"/></svg>Proven Track<br>Record</div><p class="desc">Validated through years of research and<br>thousands of clinical samples.</p></div>
  <div class="stat" style="left:869px"><div class="num">160+</div><div class="lbl"><svg width="48" height="46" viewBox="0 0 48 46" fill="none" stroke="#3a86d9" stroke-width="2"><path d="M4 24l10-10 10 6 10-6 10 10-14 14-6-4z"/><path d="M24 4v8"/></svg>Trusted<br>Partnerships</div><p class="desc">Collaborating with leading hospitals,<br>universities, and industry partners.</p></div>
</section>

<section class="product">
  <div class="scene" role="img" aria-label="Doctor and patient reviewing results on a tablet"></div>
  <div class="glow" style="left:-60px;top:300px;width:180px;height:180px"></div>
  <h2>Introducing<br>ThornaSCAN™</h2>
  <p>ThornaSCAN™ is our first urine-based test designed for individuals at higher risk of pancreatic cancer.<br>&nbsp;Validated with over 1,000 samples and supported by leading UK hospitals, ThornaSCAN™ delivers actionable results that guide earlier intervention.</p>
  <span class="btn product-cta">Request A Demo <i class="dot"></i></span>
</section>

<section>
  <h2 class="services-title">Future &amp; Supporting Services</h2>
  <div class="service" style="left:150px">
    <div class="img" role="img" aria-label="Glowing blue and pink DNA helix" style="background:linear-gradient(135deg,#1340a8,#2f8fe6 50%,#b14fd0)"></div>
    <h3>Pipeline Diagnostics</h3>
    <ul><li>Future early cancer detection tests.</li><li>Genetic predisposition testing.</li><li>Cancer risk score development.</li></ul>
    <div class="read">READ MORE <span></span></div>
  </div>
  <div class="service" style="left:455px">
    <div class="img" role="img" aria-label="Hands typing on a laptop beside printed charts" style="background:linear-gradient(160deg,#7d8388,#3f4347 60%,#2b2d30)"></div>
    <h3>Technology Platform</h3>
    <ul><li>Biomarker panels (urine &amp; serum).</li><li>AI-powered analytics for detection.</li><li>Patented technology in multiple regions.</li></ul>
    <div class="read">READ MORE <span></span></div>
  </div>
  <div class="service" style="left:763px">
    <div class="img" role="img" aria-label="Two scientists working with test tubes in a laboratory" style="background:linear-gradient(160deg,#e6ecf1,#b9c6d3 60%,#8e9fb2)"></div>
    <h3>Science &amp; Clinical Validation</h3>
    <ul><li>Published studies and trials.</li><li>Collaborations with top hospitals &amp; universities.</li></ul>
    <div class="read">READ MORE <span></span></div>
  </div>
  <div class="service" style="left:1068px">
    <div class="img" role="img" aria-label="Two people shaking hands" style="background:linear-gradient(160deg,#dfe4ea,#c9a896 60%,#a9b4c2)"></div>
    <h3>Partnerships &amp; Collaborations</h3>
    <ul><li>Academic &amp; clinical partners.</li><li>Commercial collaboration portals, testing services.</li><li>Licensing, distribution opportunities.</li></ul>
    <div class="read">READ MORE <span></span></div>
  </div>
  <span class="btn services-cta">Discover More <i class="dot"></i></span>
</section>

<section>
  <h2 class="partner-title">Your Partner In Advanced Cancer Diagnostics</h2>
  <div class="ring" style="left:247px">
    <svg width="210" height="210" viewBox="0 0 210 210"><circle cx="105" cy="105" r="100" fill="none" stroke="#e6e9ed" stroke-width="6"/><circle cx="105" cy="105" r="100" fill="none" stroke="#f6c02c" stroke-width="6" stroke-dasharray="565 628" transform="rotate(-90 105 105)"/></svg>
    <div class="txt"><span class="pct">90%</span><span class="cap">Biotech</span></div>
  </div>
  <div class="ring" style="left:495px">
    <svg width="210" height="210" viewBox="0 0 210 210"><circle cx="105" cy="105" r="100" fill="none" stroke="#e6e9ed" stroke-width="6"/><circle cx="105" cy="105" r="100" fill="none" stroke="#f6c02c" stroke-width="6" stroke-dasharray="597 628" transform="rotate(-90 105 105)"/></svg>
    <div class="txt"><span class="pct">95%</span><span class="cap">Medical<br>Research</span></div>
  </div>
  <div class="ring" style="left:744px">
    <svg width="210" height="210" viewBox="0 0 210 210"><circle cx="105" cy="105" r="100" fill="none" stroke="#e6e9ed" stroke-width="6"/><circle cx="105" cy="105" r="100" fill="none" stroke="#f6c02c" stroke-width="6" stroke-dasharray="584 628" transform="rotate(-90 105 105)"/></svg>
    <div class="txt"><span class="pct">93%</span><span class="cap">Advance<br>Treatment</span></div>
  </div>
</section>

<section>
  <h2 class="blog-title">Blog &amp; News</h2>
  <span class="btn blog-cta">Discover More <i class="dot"></i></span>
  <div class="post" style="left:150px"><div class="img" role="img" aria-label="Blue DNA strand illustration" style="background:linear-gradient(135deg,#041a3d,#1a5fc0 55%,#0a2a5a)"></div><div class="meta"><span>Admin</span><span>October 3, 2024</span></div><h4>Lorem Ipsum Dolor Sit Amet Consectetur. Leo Nec Quis Iaculis.</h4></div>
  <div class="post" style="left:379px"><div class="img" role="img" aria-label="Blue virus particle on a light background" style="background:radial-gradient(circle,#1e5cb8 0%,#6fb1ea 50%,#e6f2fb 85%)"></div><div class="meta"><span>Admin</span><span>October 3, 2024</span></div><h4>Lorem Ipsum Dolor Sit Amet Consectetur. Eu Netus Lorem.</h4></div>
  <div class="post" style="left:609px"><div class="img" role="img" aria-label="Doctor consulting with a patient in a clinic" style="background:linear-gradient(160deg,#eef1f4,#c8d1db 60%,#9aa9bb)"></div><div class="meta"><span>Admin</span><span>October 3, 2024</span></div><h4>Lorem Ipsum Dolor Sit Amet</h4></div>
  <div class="post" style="left:838px"><div class="img" role="img" aria-label="Purple DNA helix on a dark background" style="background:linear-gradient(135deg,#2a1038,#8a3aa8 55%,#3b1550)"></div><div class="meta"><span>Admin</span><span>October 3, 2024</span></div><h4>Lorem Ipsum Dolor Sit Amet</h4></div>
</section>

<footer class="footer">
  <div class="glow" style="left:1040px;top:40px;width:140px;height:140px"></div>
  <div class="glow" style="left:10px;top:380px;width:120px;height:120px"></div>
  <div class="logo"><span class="mark"></span>Velmar DX</div>
  <div class="links"><span>Home</span><span>About Us</span><span>Products / Service</span><span>News</span><span>Contact</span></div>
  <span class="btn footer-cta">Get Started <i class="dot"></i></span>
  <div class="social" aria-label="Social media links"><span></span><span></span><span></span></div>
  <div class="rule"></div>
  <p class="legal" style="left:150px">Copyright © 2025. All Rights Reserved.</p>
  <p class="legal" style="left:786px">General Terms And Conditions Of Business &nbsp;&nbsp; Privacy Policy</p>
</footer>

</body>
</html>
```